1 Page for Computer Repair Website

Looking for a 1 page website with a design that compliments the business card and pamphlet that have already been made (attached files). It should look business professional and easy to read. Email and phone number should be somewhere near the top of the website, visible when the page loads. I don't want any forms for people to mess with. No "Contact Us" form or entering in email for newsletter. Customers will just be looking at this site to confirm we are professionals and have our business in order.

Target Market(s)

Home and small business

Industry/Entity Type

Computer Repair

Coding

Coded - Design and coding required

Number of Pages Required

1 page

Font styles to use
Other font styles liked:
• Helvetica variations used in pamphlet and card

Colors
0455a3
cfdeed
85abd2
3276b5
85cae6
ffffff

Requirements
Must have
• Compliment the pamphlet and business card in color choices and font use. Pleasing to the eye and easy to read through categories and text.
Should not have
• Forms. No "enter name and email here" or anything of the sort.

```html
<!DOCTYPE html>
<html lang="en">
<head>
<meta charset="utf-8">
<title>Bytefix Computer Service</title>
<link href="https://fonts.googleapis.com/css2?family=Roboto:wght@300;400;500;700&display=swap" rel="stylesheet">
<style>
:root{
  --brand:#0455a3;
  --brand-deep:#0b3c78;
  --brand-mid:#3276b5;
  --brand-soft:#85abd2;
  --brand-sky:#85cae6;
  --brand-pale:#cfdeed;
  --white:#ffffff;
  --ink:#1f2a3c;
  --text:#5d6470;
  --hero-bg:#f1ecec;
  --nav:#0e2d57;
  --nav-active:#8e9299;
  --services-bg:#1c2129;
  --card-hover:#8d9095;
  --arrow-btn:#7c8189;
  --footer:#2d2d2f;
  --footer-bottom:#1b1b1c;
}
*{box-sizing:border-box;margin:0;padding:0}
html,body{width:1200px;height:2676px;overflow:hidden}
body{font-family:"Roboto",Helvetica,Arial,sans-serif;background:var(--white);color:var(--text);position:relative}
.container{width:1104px;margin:0 auto;position:relative}

/* header */
.site-header{height:120px}
.site-header .container{height:120px;display:flex;align-items:center;justify-content:space-between}
.logo{display:flex;flex-direction:column;line-height:1}
.logo-name{font-size:44px;font-weight:700;color:var(--nav);letter-spacing:1px}
.logo-tag{font-size:15px;font-weight:400;color:var(--brand-mid);margin-top:4px;letter-spacing:.5px}
.top-contact{display:flex;gap:40px;align-items:center;margin-top:-40px;font-size:15px;font-weight:500;color:var(--nav)}
.top-contact span{display:flex;align-items:center;gap:8px}

/* nav */
.main-nav{height:68px}
.main-nav .container{background:var(--nav);height:68px;display:flex}
.main-nav a{display:flex;align-items:center;justify-content:center;width:120px;font-size:13px;font-weight:500;color:var(--white);text-decoration:none;letter-spacing:.5px}
.main-nav a.active{background:var(--nav-active);width:104px}
.main-nav a:first-child{}

/* hero */
.hero{height:632px;background:var(--hero-bg);position:relative}
.hero-copy{position:absolute;left:48px;top:200px;width:470px}
.hero-copy h1{font-size:44px;font-weight:700;color:var(--ink);line-height:1.1}
.hero-copy h2{font-size:27px;font-weight:400;color:var(--ink);margin-top:10px}
.hero-copy p{font-size:13px;line-height:1.6;margin-top:18px}
.btn{display:inline-block;margin-top:22px;background:var(--nav);color:var(--white);font-size:13px;font-weight:500;padding:12px 18px;letter-spacing:.5px}
.hero-visual{position:absolute;left:520px;top:56px;width:640px;height:520px;border-radius:6px;background:radial-gradient(ellipse at 45% 45%,#ffffff 0%,#e4e2e4 55%,#d8d4d6 100%)}

/* about */
.about{height:228px;text-align:center;padding-top:44px}
.section-title{font-size:34px;font-weight:500;color:var(--ink)}
.about p{width:1000px;margin:18px auto 0;font-size:12.5px;line-height:1.7}

/* services */
.services{height:992px;position:relative;background:var(--services-bg)}
.services-bg{position:absolute;inset:0;background:linear-gradient(160deg,#2a3038 0%,#181c22 50%,#252a31 100%)}
.services .section-title{position:relative;color:var(--white);text-align:center;padding-top:48px}
.service-grid{position:absolute;left:48px;top:132px;width:1104px;display:grid;grid-template-columns:540px 540px;column-gap:24px;row-gap:22px}
.service-card{height:188px;background:var(--brand-deep);position:relative;padding:32px 40px 0 124px;color:var(--white)}
.service-card.is-highlighted{background:var(--card-hover)}
.service-icon{position:absolute;left:30px;top:36px;width:66px;height:66px;border:2px solid var(--white);border-radius:50%;display:flex;align-items:center;justify-content:center}
.service-card.is-highlighted .service-icon{background:var(--white);border-color:var(--white)}
.service-card h3{font-size:21px;font-weight:500}
.service-card p{font-size:12.5px;line-height:1.55;margin-top:10px;color:var(--brand-pale)}
.service-card.is-highlighted p{color:#f0f0f0}
.card-arrow{position:absolute;right:0;bottom:0;width:32px;height:32px;background:var(--arrow-btn);display:flex;align-items:center;justify-content:center}
.service-card.is-highlighted .card-arrow{background:var(--brand-deep)}

/* why */
.why{height:420px;position:relative}
.why .section-title{text-align:center;padding-top:76px}
.why-visual{position:absolute;left:48px;top:164px;width:472px;height:200px;background:linear-gradient(120deg,#5d6a7a 0%,#b9c4cf 50%,#dfe5ea 100%)}
.why-list{position:absolute;left:564px;top:160px;width:588px;list-style:none}
.why-list li{position:relative;padding-left:18px;font-size:12.5px;line-height:1.55;margin-bottom:12px}
.why-list li::before{content:"";position:absolute;left:0;top:7px;width:6px;height:6px;border-radius:50%;background:var(--brand-mid)}

/* footer */
.site-footer{position:absolute;left:0;top:2460px;width:1200px;height:216px;background:var(--footer);color:var(--white)}
.footer-contact{display:flex;justify-content:space-between;align-items:center;height:120px;padding:0 48px;border-bottom:1px solid #444}
.footer-item{display:flex;align-items:center;gap:14px;font-size:22px;font-weight:400;line-height:1.2}
.footer-item .ring{width:36px;height:36px;border:2px solid var(--white);border-radius:50%;display:flex;align-items:center;justify-content:center;flex-shrink:0}
.footer-bottom{position:absolute;left:0;bottom:0;width:1200px;height:96px;background:var(--footer-bottom);text-align:center;padding-top:28px}
.footer-links{font-size:12px;color:#ddd}
.footer-links a{color:#ddd;text-decoration:none;margin:0 4px}
.copyright{font-size:11px;color:#8a8a8a;margin-top:8px}
.social{position:absolute;right:48px;top:30px;display:flex;gap:10px}
.social span{width:30px;height:30px;border-radius:50%;background:#4a4a4d;display:block}
</style>
</head>
<body>

<header class="site-header">
  <div class="container">
    <div class="logo">
      <span class="logo-name">BYTEFIX</span>
      <span class="logo-tag">Computer Service</span>
    </div>
    <div class="top-contact">
      <span><svg width="16" height="12" viewBox="0 0 16 12"><rect x="0.5" y="0.5" width="15" height="11" fill="none" stroke="#0e2d57"/><path d="M1 1l7 6 7-6" fill="none" stroke="#0e2d57"/></svg>info@bytefix-service.com</span>
      <span><svg width="14" height="14" viewBox="0 0 24 24"><path d="M6.6 10.8a15 15 0 006.6 6.6l2.2-2.2a1 1 0 011-.25 11.4 11.4 0 003.6.6 1 1 0 011 1V20a1 1 0 01-1 1A17 17 0 013 4a1 1 0 011-1h3.5a1 1 0 011 1 11.4 11.4 0 00.6 3.6 1 1 0 01-.25 1z" fill="#0e2d57"/></svg>(123) 456-7890</span>
    </div>
  </div>
</header>

<nav class="main-nav">
  <div class="container">
    <a class="active" href="#">HOME</a>
    <a href="#">ABOUT US</a>
    <a href="#">SERVICE</a>
    <a href="#">PRICE</a>
    <a href="#">NEWS</a>
    <a href="#">CONTACT US</a>
  </div>
</nav>

<section class="hero">
  <div class="hero-visual" role="img" aria-label="Hand holding a wrench reaching out of a computer monitor, with keyboard and mouse"></div>
  <div class="hero-copy">
    <h1>Any computer problems?</h1>
    <h2>Receive instant service!</h2>
    <p>Slow startup, strange pop-ups or a screen that will not wake? Our certified technicians diagnose the fault quickly, explain the fix in plain language and get your home or office computer working again, often the same day.</p>
    <span class="btn">READ MORE</span>
  </div>
</section>

<section class="about">
  <h2 class="section-title">About Us</h2>
  <p>Our shop has served homes and small businesses for more than ten years. Every repair is handled by trained technicians who test each part, protect your files and keep you informed at every step. We quote before we work, use quality replacement parts and stand behind every job with a clear written warranty. Drop by the shop or call us and we will come to you.</p>
</section>

<section class="services">
  <div class="services-bg" role="img" aria-label="Dark close-up of computer hardware components"></div>
  <h2 class="section-title">Our Services</h2>
  <div class="service-grid">

    <article class="service-card">
      <div class="service-icon"><svg width="32" height="28" viewBox="0 0 32 28"><rect x="2" y="2" width="28" height="18" rx="1" fill="none" stroke="#fff" stroke-width="2.5"/><path d="M11 26h10M16 20v6" stroke="#fff" stroke-width="2.5"/></svg></div>
      <h3>PC/Laptop Hardware Repair</h3>
      <p>Broken screens, failing drives, dead power jacks and noisy fans replaced with quality parts and tested before the machine goes back to you.</p>
      <span class="card-arrow"><svg width="10" height="12" viewBox="0 0 10 12"><path d="M1 0l8 6-8 6z" fill="#fff"/></svg></span>
    </article>

    <article class="service-card is-highlighted">
      <div class="service-icon"><svg width="34" height="34" viewBox="0 0 34 34"><path d="M17 3l12 5v8c0 8-5 13-12 15C10 29 5 24 5 16V8z" fill="#0b3c78"/><path d="M11 17l4 4 8-8" fill="none" stroke="#fff" stroke-width="2.5"/></svg></div>
      <h3>Malware Removal</h3>
      <p>Viruses, spyware and unwanted pop-ups cleaned out completely, then we install solid protection so your computer stays safe and fast.</p>
      <span class="card-arrow"><svg width="10" height="12" viewBox="0 0 10 12"><path d="M1 0l8 6-8 6z" fill="#fff"/></svg></span>
    </article>

    <article class="service-card">
      <div class="service-icon"><svg width="34" height="34" viewBox="0 0 34 34"><circle cx="13" cy="19" r="7" fill="none" stroke="#fff" stroke-width="3" stroke-dasharray="3 2.5"/><circle cx="13" cy="19" r="2.5" fill="#fff"/><circle cx="25" cy="10" r="5" fill="none" stroke="#fff" stroke-width="2.5" stroke-dasharray="2.5 2"/></svg></div>
      <h3>Hard/Software Upgrades</h3>
      <p>Faster storage, more memory and current software installed and configured, giving older computers years of extra useful life.</p>
      <span class="card-arrow"><svg width="10" height="12" viewBox="0 0 10 12"><path d="M1 0l8 6-8 6z" fill="#fff"/></svg></span>
    </article>

    <article class="service-card">
      <div class="service-icon"><svg width="26" height="32" viewBox="0 0 26 32"><path d="M2 2h15l7 7v21H2z" fill="none" stroke="#fff" stroke-width="2.5"/><path d="M7 15h12M7 20h12M7 25h8" stroke="#fff" stroke-width="2"/></svg></div>
      <h3>Data Migration</h3>
      <p>Files, photos, email and settings moved safely from your old computer to the new one, checked so nothing is left behind.</p>
      <span class="card-arrow"><svg width="10" height="12" viewBox="0 0 10 12"><path d="M1 0l8 6-8 6z" fill="#fff"/></svg></span>
    </article>

    <article class="service-card">
      <div class="service-icon"><svg width="34" height="34" viewBox="0 0 34 34"><circle cx="17" cy="17" r="13" fill="none" stroke="#fff" stroke-width="2.5"/><circle cx="17" cy="17" r="6" fill="none" stroke="#fff" stroke-width="2.5"/><path d="M8 8l5 5M26 8l-5 5M8 26l5-5M26 26l-5-5" stroke="#fff" stroke-width="2.5"/></svg></div>
      <h3>Clean/tune ups</h3>
      <p>Dust removed, startup trimmed and updates applied so your system runs cooler, boots quicker and responds the way it should.</p>
      <span class="card-arrow"><svg width="10" height="12" viewBox="0 0 10 12"><path d="M1 0l8 6-8 6z" fill="#fff"/></svg></span>
    </article>

    <article class="service-card">
      <div class="service-icon"><svg width="32" height="32" viewBox="0 0 32 32"><path d="M16 3l3 8 8 3-8 3-3 8-3-8-8-3 8-3z" fill="#fff"/></svg></div>
      <h3>Data Rescue</h3>
      <p>Lost files recovered from failed drives, deleted folders and damaged memory cards, handled carefully to give the best chance of success.</p>
      <span class="card-arrow"><svg width="10" height="12" viewBox="0 0 10 12"><path d="M1 0l8 6-8 6z" fill="#fff"/></svg></span>
    </article>

    <article class="service-card">
      <div class="service-icon"><svg width="32" height="30" viewBox="0 0 32 30"><path d="M16 3L2 15h4v12h8v-8h4v8h8V15h4z" fill="#fff"/></svg></div>
      <h3>In-Home Installation</h3>
      <p>We come to you to set up computers, printers and home networks, then show you how everything works before we leave.</p>
      <span class="card-arrow"><svg width="10" height="12" viewBox="0 0 10 12"><path d="M1 0l8 6-8 6z" fill="#fff"/></svg></span>
    </article>

    <article class="service-card">
      <div class="service-icon"><svg width="22" height="32" viewBox="0 0 22 32"><path d="M14 2L3 18h7l-3 12 12-17h-7z" fill="#fff"/></svg></div>
      <h3>Remote Support</h3>
      <p>Quick fixes over a secure connection for software problems, settings and questions, without you needing to leave your desk.</p>
      <span class="card-arrow"><svg width="10" height="12" viewBox="0 0 10 12"><path d="M1 0l8 6-8 6z" fill="#fff"/></svg></span>
    </article>

  </div>
</section>

<section class="why">
  <h2 class="section-title">Why Choose Us</h2>
  <div class="why-visual" role="img" aria-label="Technician working on a desktop computer at a repair bench"></div>
  <ul class="why-list">
    <li>Certified technicians with years of hands-on experience repairing laptops, desktops and small office networks of every brand.</li>
    <li>Free diagnosis and a clear written quote before any work begins, so you never face surprise charges at pickup.</li>
    <li>Most repairs completed within one to two days, with same-day service available for urgent business needs.</li>
    <li>Your files and privacy are protected at every step, and every repair comes with a ninety day warranty.</li>
    <li>Friendly local service for homes and small businesses, with on-site visits and remote help when you need it.</li>
  </ul>
</section>

<footer class="site-footer">
  <div class="footer-contact">
    <div class="footer-item">
      <span class="ring"><svg width="14" height="18" viewBox="0 0 14 18"><path d="M7 1a6 6 0 016 6c0 4-6 10-6 10S1 11 1 7a6 6 0 016-6z" fill="#fff"/><circle cx="7" cy="7" r="2.2" fill="#2d2d2f"/></svg></span>
      <span>Address Line1, Address Line2<br>Country - 123456</span>
    </div>
    <div class="footer-item">
      <span class="ring"><svg width="16" height="16" viewBox="0 0 24 24"><path d="M6.6 10.8a15 15 0 006.6 6.6l2.2-2.2a1 1 0 011-.25 11.4 11.4 0 003.6.6 1 1 0 011 1V20a1 1 0 01-1 1A17 17 0 013 4a1 1 0 011-1h3.5a1 1 0 011 1 11.4 11.4 0 00.6 3.6 1 1 0 01-.25 1z" fill="#fff"/></svg></span>
      <span>(123) 456-7890</span>
    </div>
    <div class="footer-item">
      <span class="ring"><svg width="16" height="12" viewBox="0 0 16 12"><rect x="0.5" y="0.5" width="15" height="11" fill="none" stroke="#fff"/><path d="M1 1l7 6 7-6" fill="none" stroke="#fff"/></svg></span>
      <span>info@bytefix-service.com</span>
    </div>
  </div>
  <div class="footer-bottom">
    <div class="footer-links"><a href="#">Home</a>| <a href="#">About Us</a>| <a href="#">Our Service</a>| <a href="#">Price</a>| <a href="#">News</a>| <a href="#">Contact Us</a></div>
    <div class="copyright">© 2024 Bytefix Computer Service. All rights reserved.</div>
    <div class="social"><span></span><span></span><span></span><span></span></div>
  </div>
</footer>

</body>
</html>
```